Rehab/fitness Business card design

I need a design that promotes "A ready made base for runners". services include assessment, massage, physiotherapy, pilates, suspension training, kinesiotaping in any combination.
I would like to bring the design into my website, flyers etc

Target Market(s)

athletes from beginner to elite - any age, male and female

Industry/Entity Type

Shop

Contact Information for Business Card

Ready-Made-Base for Runners
17 Parvel Crescent, Hollowmere, Tauranga
021 847 3610
gwen.farrowby@quillmail.test

Logo Text

Requirements
Nice to have
• Blue colour theme

```html
<!DOCTYPE html>
<html lang="en">
<head>
<meta charset="UTF-8">
<title>Ready-Made-Base for Runners — Business Card</title>
<link href="https://fonts.googleapis.com/css2?family=Josefin+Sans:wght@400&family=Open+Sans:wght@400&display=swap" rel="stylesheet">
<style>
  :root {
    --page-bg: #ecebe8;
    --navy: #1e1b5c;
    --navy-text: #26236a;
    --card-light: #f7f7f7;
    --card-light-edge: #e2e2e4;
    --back-center: #2f3f98;
    --back-edge: #1f1d62;
    --heading-tint: #b9bbe6;
    --white: #ffffff;
    --emblem-tint: rgba(70, 70, 150, 0.07);
  }
  * { margin: 0; padding: 0; box-sizing: border-box; }
  html, body {
    width: 1200px;
    height: 1181px;
    overflow: hidden;
    background: var(--page-bg);
  }
  .canvas {
    position: relative;
    width: 1200px;
    height: 1181px;
  }
  .card {
    position: absolute;
    left: 209px;
    width: 781px;
    height: 449px;
    border-radius: 30px;
    overflow: hidden;
  }
  .card-front {
    top: 110px;
    background: radial-gradient(ellipse at 50% 50%, var(--card-light) 0%, var(--card-light) 35%, var(--card-light-edge) 100%);
  }
  .front-tab {
    position: absolute;
    left: 114px;
    width: 554px;
    height: 18px;
    background: var(--navy);
  }
  .front-tab-top { top: 0; border-radius: 0 0 6px 6px; }
  .front-tab-bottom { bottom: 0; border-radius: 6px 6px 0 0; }
  .emblem-area {
    position: absolute;
    left: 280px;
    top: 100px;
    width: 240px;
    height: 240px;
    border-radius: 50%;
    background: var(--emblem-tint);
  }
  .card-back .emblem-area {
    background: rgba(255, 255, 255, 0.04);
    top: 95px;
  }
  .business-name {
    position: absolute;
    left: 0;
    right: 0;
    top: 202px;
    text-align: center;
    font-family: "Josefin Sans", sans-serif;
    font-variant: small-caps;
    font-size: 38px;
    letter-spacing: 4px;
    color: var(--navy-text);
  }
  .card-back {
    top: 611px;
    background: radial-gradient(ellipse at 50% 40%, var(--back-center) 0%, var(--back-edge) 70%);
    font-family: "Open Sans", sans-serif;
    text-align: center;
    color: var(--white);
  }
  .services-heading {
    position: absolute;
    left: 0; right: 0;
    top: 184px;
    font-size: 24px;
    color: var(--heading-tint);
  }
  .services-list {
    position: absolute;
    left: 0; right: 0;
    top: 223px;
    list-style: none;
    font-size: 17.5px;
    line-height: 22px;
    letter-spacing: 0.5px;
  }
  .contact {
    position: absolute;
    left: 0; right: 0;
    top: 386px;
    font-style: normal;
    font-size: 13.5px;
    line-height: 16.5px;
    letter-spacing: 0.3px;
  }
</style>
</head>
<body>
  <main class="canvas">
    <section class="card card-front">
      <div class="front-tab front-tab-top"></div>
      <div class="emblem-area" role="img" aria-label="Faint brand emblem area"></div>
      <h1 class="business-name">Ready-Made-Base for Runners</h1>
      <div class="front-tab front-tab-bottom"></div>
    </section>

    <section class="card card-back">
      <div class="emblem-area" role="img" aria-label="Faint brand emblem area"></div>
      <h2 class="services-heading">SERVICES OFFERED</h2>
      <ul class="services-list">
        <li>Assessment – Massage</li>
        <li>Physiotherapy – Pilates – Suspension training</li>
        <li>Kinesiotaping in any combination</li>
      </ul>
      <address class="contact">
        17 Parvel Crescent, Hollowmere, Tauranga<br>
        021 847 3610<br>
        gwen.farrowby@quillmail.test
      </address>
    </section>
  </main>
</body>
</html>
```